Tall Maple website Laser Like Lipo and Facial Rejuvenation busines

I need a website for my Laser Like Lipo and Facial Rejuvenation business called Tall Maple. I purchased the domain name. I have a logo and before and after pictures to include along with basic information about the procedure and pricing information. I would like my website to be used by customers to be able to schedule appointments. My logo and before-and-after pictures are attached.

My business is called Tall Maple. It is a laser like Lipo and facial rejuvenation. I've attached my logo and before and after pictures to use on the website.

These treatments are non invasive and people lose 2-10 inches per treatment. My primary audience will be overweight women 30 years of age or older or those with cellulite. I will have some male customers too but mostly women.

As for the web design, I've never had a website before so I really don't have anything specific in mind. I'm open to considering anything. I'm not a girly, girl and I don't like frilly, fancy stuff. I just want something simple but not to either. I love my logo. That is a great fit for my business and personality. I have increased the budget to include coding.

I do not like pastel colors. I do need colors that compliment my logo.

Target Market(s)

Mostly over weight Women or those with cellulite ages 30 and above. Some men.

Industry/Entity Type

Business

Coding

Coded - Design and coding required

Number of Pages Required

3 page

Font styles to use
Serif

Requirements
Must have
• I want my logo and information section on one page, a page for before and after pictures that enlarge when clicked on. I do not want a slide show, and a page for prices. I previously mentioned a section for them to schedule appointments but have decided that I don't want that.
• I do not like pastel colors. I do need colors that compliment my logo.
Should not have
• Not a slide show

```html
<!DOCTYPE html>
<html lang="en">
<head>
<meta charset="utf-8">
<title>Tall Maple – Laser Like Lipo &amp; Facial Rejuvenation</title>
<link rel="stylesheet" href="https://fonts.googleapis.com/css2?family=Open+Sans:wght@400;600;700&family=Raleway:wght@400;600;700&display=swap">
<style>
:root{
  --red:#b3141b;
  --red-dark:#8e0f14;
  --ink:#2b2b2b;
  --charcoal:#333333;
  --muted:#666666;
  --light:#f3f3f3;
  --white:#ffffff;
  --hero-brown:#4a3326;
  --footer:#1f1f1f;
}
*{box-sizing:border-box;margin:0;padding:0}
html,body{width:1200px;height:2304px;overflow:hidden}
body{font-family:"Open Sans",Arial,sans-serif;color:var(--ink);background:var(--white)}
.container{width:1000px;margin:0 auto;position:relative}

/* header */
.site-header{height:120px}
.site-header .container{height:120px;display:flex;align-items:center;justify-content:space-between}
.brand{display:flex;align-items:center;gap:14px}
.brand-mark{width:22px;height:22px;background:var(--red)}
.brand-name{font-family:"Raleway",sans-serif;font-weight:700;font-size:40px;color:var(--red);letter-spacing:1px}
.brand-tag{font-size:11px;color:var(--muted);letter-spacing:2px;text-transform:uppercase;margin-top:4px}
.phone{text-align:right;color:var(--red);font-family:"Raleway",sans-serif}
.phone-line{display:flex;align-items:center;gap:10px;font-size:28px;font-weight:600}

/* navigation */
.main-nav{background:var(--red);height:40px}
.main-nav .container{height:40px;display:flex;align-items:center;justify-content:space-between}
.nav-links{display:flex;list-style:none;gap:30px}
.nav-links li{color:var(--white);font-size:13px;font-weight:600}
.search{width:170px;height:26px;background:var(--white);display:flex;align-items:center;justify-content:space-between;padding:0 8px;font-size:12px;color:var(--muted)}

/* hero */
.hero{height:460px;position:relative;background:linear-gradient(90deg,#c7a486 0%,#8b6348 38%,var(--hero-brown) 60%,#2e1f17 100%)}
.hero-photo{position:absolute;left:100px;top:0;width:440px;height:460px;background:radial-gradient(ellipse at 45% 45%,#e6c3a5 0%,#b88763 45%,rgba(110,75,52,0) 75%)}
.hero-copy{position:absolute;left:600px;top:150px;width:420px;text-align:center;color:var(--white)}
.hero-copy h1{font-family:"Raleway",sans-serif;font-weight:400;font-size:30px;line-height:1.35}
.hero-brand{margin-top:34px;font-family:"Raleway",sans-serif;font-weight:700;font-size:34px;color:var(--white)}

/* welcome band */
.welcome{background:var(--red);height:140px}
.welcome .container{height:140px;display:flex;align-items:center;justify-content:space-between}
.welcome h2{font-family:"Raleway",sans-serif;font-weight:600;font-size:34px;color:var(--white)}
.welcome p{font-size:15px;color:var(--white);margin-top:6px}
.btn-dark{background:var(--charcoal);color:var(--white);font-size:15px;font-weight:700;padding:16px 22px;text-transform:uppercase}

/* service cards */
.services{padding-top:20px;height:370px}
.services .container{display:flex;gap:20px}
.card{width:320px}
.card-photo{height:140px}
.card h3{color:var(--red);font-size:12px;font-weight:700;line-height:1.4;margin-top:12px}
.card p{font-size:11px;color:var(--muted);line-height:1.55;margin-top:8px}
.btn-small{display:inline-block;margin-top:14px;background:var(--charcoal);color:var(--white);font-size:11px;font-weight:700;padding:7px 12px;text-transform:uppercase}

/* testimonials */
.testimonials{height:290px;background:linear-gradient(180deg,#3a3a3a,#4d4d4d 50%,#3a3a3a);color:var(--white);text-align:center;padding-top:20px}
.testimonials h2{font-family:"Raleway",sans-serif;font-weight:600;font-size:24px}
.avatar{width:76px;height:76px;border-radius:50%;margin:14px auto 0;background:linear-gradient(135deg,#d9b79b,#8d6a55);border:3px solid var(--white)}
.testimonials blockquote{width:720px;margin:18px auto 0;font-size:12px;line-height:1.6;color:#dddddd}
.testimonials cite{display:block;margin-top:14px;font-style:italic;font-size:13px}

/* before & after */
.results{height:380px;padding-top:30px}
.results h2{text-align:center;font-family:"Raleway",sans-serif;font-weight:700;font-size:26px;color:var(--red)}
.pairs{display:flex;gap:20px;margin-top:30px}
.pair{width:320px}
.pair-photos{display:flex;gap:6px}
.pair-photo{width:157px;height:190px;background:linear-gradient(180deg,#e8c8a8,#b27c56)}
.pair-photo.dark{background:linear-gradient(180deg,#6b5a50,#a07a5e)}
.pair-labels{display:flex;justify-content:space-around;font-size:12px;font-weight:700;margin-top:10px}
.pair-caption{font-size:12px;font-weight:700;text-align:center;margin-top:10px;border-top:1px solid #dddddd;padding-top:10px}

/* contact */
.contact{height:434px;position:relative;background:linear-gradient(160deg,#e9ece6,#dfe3dd 50%,#e6e8e2)}
.contact-panel{position:absolute;left:260px;top:18px;width:680px;text-align:center}
.contact h2{font-family:"Raleway",sans-serif;font-weight:700;font-size:26px;color:var(--red)}
.contact h3{font-size:15px;font-weight:600;margin-top:8px}
.contact p{font-size:12px;color:var(--muted);line-height:1.6;width:520px;margin:12px auto 0}
.form{display:grid;grid-template-columns:300px 300px;gap:10px 16px;justify-content:center;margin-top:22px;text-align:left}
.field{height:34px;background:#9a9a9a;color:var(--white);font-size:12px;padding:9px 12px}
.field.message{grid-row:2 / span 2;grid-column:2;height:78px}
.submit{display:inline-block;margin-top:14px;background:var(--charcoal);color:var(--white);font-size:12px;font-weight:700;padding:9px 18px;text-transform:uppercase}
.socials{display:flex;justify-content:center;gap:10px;margin-top:18px}
.socials span{width:36px;height:36px;border-radius:50%;background:#4a68a6}

/* footer */
.site-footer{height:60px;background:var(--footer);color:#bbbbbb;font-size:12px}
.site-footer .container{height:60px;display:flex;align-items:center;justify-content:space-between}
.footer-links{display:flex;gap:24px;list-style:none}
</style>
</head>
<body>

<header class="site-header">
  <div class="container">
    <div>
      <div class="brand"><span class="brand-mark"></span><span class="brand-name">Tall Maple</span></div>
      <div class="brand-tag">Laser Like Lipo &amp; Facial Rejuvenation</div>
    </div>
    <div class="phone">
      <div class="phone-line">
        <svg width="22" height="22" viewBox="0 0 24 24" aria-hidden="true"><path fill="#b3141b" d="M6.6 10.8a15 15 0 0 0 6.6 6.6l2.2-2.2a1 1 0 0 1 1-.25 11.4 11.4 0 0 0 3.6.57 1 1 0 0 1 1 1V20a1 1 0 0 1-1 1A17 17 0 0 1 3 4a1 1 0 0 1 1-1h3.5a1 1 0 0 1 1 1c0 1.25.2 2.45.57 3.57a1 1 0 0 1-.25 1z"/></svg>
        1-800 555 0142
      </div>
    </div>
  </div>
</header>

<nav class="main-nav">
  <div class="container">
    <ul class="nav-links">
      <li>Home</li><li>About us</li><li>Before &amp; After</li><li>Prices</li><li>Schedule Appointments</li><li>Contact us</li>
    </ul>
    <div class="search">Search
      <svg width="12" height="12" viewBox="0 0 24 24" aria-hidden="true"><circle cx="10" cy="10" r="7" fill="none" stroke="#666" stroke-width="3"/><line x1="15" y1="15" x2="22" y2="22" stroke="#666" stroke-width="3"/></svg>
    </div>
  </div>
</nav>

<section class="hero">
  <div class="hero-photo" role="img" aria-label="Portrait of a smiling woman with long brown hair"></div>
  <div class="hero-copy">
    <h1>We provide Laser Like Lipo and Facial Rejuvenation.</h1>
    <div class="hero-brand">Tall Maple</div>
  </div>
</section>

<section class="welcome">
  <div class="container">
    <div>
      <h2>WELCOME TO OUR LASER &amp; ANTI-AGING CENTER</h2>
      <p>The best skin rejuvenation center offering cosmetic face and body individual treatments</p>
    </div>
    <span class="btn-dark">See our offers</span>
  </div>
</section>

<section class="services">
  <div class="container">
    <article class="card">
      <div class="card-photo" role="img" aria-label="Woman receiving a facial laser treatment" style="background:linear-gradient(135deg,#e7e2de,#c9b6a8)"></div>
      <h3>NON INVASIVE LASER CONTOURING FOR A SLIMMER AND MORE CONFIDENT YOU</h3>
      <p>Our gentle laser sessions target stubborn fat without needles or downtime. Most clients lose two to ten inches per treatment and return to their day right away feeling lighter and refreshed.</p>
      <span class="btn-small">Read more</span>
    </article>
    <article class="card">
      <div class="card-photo" role="img" aria-label="Woman touching her smooth shoulder with a flower" style="background:linear-gradient(135deg,#f0d5c4,#d8a88e)"></div>
      <h3>FACIAL REJUVENATION THAT RESTORES YOUR NATURAL GLOW AND FIRMS TIRED SKIN</h3>
      <p>Light based facial care smooths fine lines, evens tone and tightens skin. Each visit is quick, comfortable and planned around your goals, so results look natural and stay with you.</p>
      <span class="btn-small">Read more</span>
    </article>
    <article class="card">
      <div class="card-photo" role="img" aria-label="Slim waist and hips of a woman in white" style="background:linear-gradient(135deg,#eadcd2,#c9a58d)"></div>
      <h3>CELLULITE REDUCTION TREATMENTS FOR SMOOTHER THIGHS HIPS AND ARMS EVERY DAY</h3>
      <p>Focused laser energy improves circulation and breaks up dimpled areas. Paired with simple lifestyle tips, our plans help you see smoother skin and firmer contours within a few weeks.</p>
      <span class="btn-small">Read more</span>
    </article>
  </div>
</section>

<section class="testimonials" role="img" aria-label="Dimmed background of a treatment room behind client testimonials">
  <h2>CLIENTS TESTIMONIALS</h2>
  <div class="avatar" role="img" aria-label="Client portrait"></div>
  <blockquote>I tried diets and gym routines for years with little change. After six sessions at Tall Maple I lost several inches around my waist and finally feel comfortable in my clothes again. The team made every visit relaxed and friendly.</blockquote>
  <cite>~ Dana Whitfield</cite>
</section>

<section class="results">
  <div class="container">
    <h2>BEFORE &amp; AFTER</h2>
    <div class="pairs">
      <div class="pair">
        <div class="pair-photos">
          <div class="pair-photo" role="img" aria-label="Waist before treatment"></div>
          <div class="pair-photo" role="img" aria-label="Waist after treatment"></div>
        </div>
        <div class="pair-labels"><span>BEFORE</span><span>AFTER</span></div>
        <div class="pair-caption">LASER LIKE LIPO TREATMENT</div>
      </div>
      <div class="pair">
        <div class="pair-photos">
          <div class="pair-photo dark" role="img" aria-label="Abdomen before treatment"></div>
          <div class="pair-photo" role="img" aria-label="Abdomen after treatment"></div>
        </div>
        <div class="pair-labels"><span>BEFORE</span><span>AFTER</span></div>
        <div class="pair-caption">LASER LIKE LIPO TREATMENT</div>
      </div>
      <div class="pair">
        <div class="pair-photos">
          <div class="pair-photo" role="img" aria-label="Torso before treatment"></div>
          <div class="pair-photo dark" role="img" aria-label="Torso after treatment"></div>
        </div>
        <div class="pair-labels"><span>BEFORE</span><span>AFTER</span></div>
        <div class="pair-caption">LASER LIKE LIPO TREATMENT</div>
      </div>
    </div>
  </div>
</section>

<section class="contact" role="img" aria-label="Faded street map behind the contact form">
  <div class="contact-panel">
    <h2>Contact Us</h2>
    <h3>It's time to look your best</h3>
    <p>If you've made it this far down the page, you are ready to consider a change. Send us a note and we will get back to you soon.</p>
    <div class="form">
      <div class="field">First Name</div>
      <div class="field">Last Name</div>
      <div class="field">Email Address</div>
      <div class="field message">Message</div>
      <div class="field">Phone Number</div>
    </div>
    <span class="submit">Submit</span>
    <div class="socials"><span></span><span></span><span></span><span></span></div>
  </div>
</section>

<footer class="site-footer">
  <div class="container">
    <ul class="footer-links">
      <li>Home</li><li>About us</li><li>Before &amp; After</li><li>Prices</li><li>Schedule Appointments</li><li>Contact us</li>
    </ul>
    <span>© 2024 Tall Maple. All rights reserved.</span>
  </div>
</footer>

</body>
</html>
```